New look while maintaining the Brand identification!

I want a new look for my business card. I want to keep the same colors and feel but change the look and layout a bit. The logo (KALMORETIX Physical therapy Reimagined and the lilypad) must remain the same and in that font.
We are a physical therapy clinic. So we have certification that we can write on the back or services we provide (which is what we currently have on the back of the card as well)

Contact information
2840 Cedar Hollow Rd., #22
Brightwater, FL 34276
P: (239) 555-0172
F: (239) 555-0198
E: kalmoretixcare@mailvexo.com
W: www.kalmoretixcare-example.com

Industry/Entity Type

Physical Therapy

Contact Information for Business Card

Our current cards have the business address and information on the back. But I am willing to have it be in the front.

Font styles to use
Sans Serif

Colors
abd036
fbf289
ec1f27

Requirements
Must have
• Has to be unique!
• Services we provide and/or techniques we do must fit on the card
Nice to have
• Would like to have the front and back somehow linked together. Such that if you set the front next to the back, there is a nice flow of design! Currently the back is white with writing on it.
Should not have
• I like the wave lines as compared to straight lines.

```html
<!DOCTYPE html>
<html lang="en">
<head>
<meta charset="utf-8">
<title>Kalmoretix Business Card</title>
<link rel="stylesheet" href="https://fonts.googleapis.com/css2?family=Oswald:wght@500&family=Montserrat:wght@400;500&display=swap">
<style>
  :root {
    --stage: #4a3a2c;
    --card: #ffffff;
    --gold: #c9b42b;
    --leaf: #abd036;
    --red: #ec1f27;
    --ink: #444444;
    --ink-dark: #222222;
  }
  * { box-sizing: border-box; margin: 0; padding: 0; }
  html, body { width: 1200px; height: 843px; overflow: hidden; }
  body { background: var(--stage); position: relative; font-family: "Montserrat", sans-serif; }

  .card {
    position: absolute;
    top: 252px;
    width: 558px;
    height: 319px;
    background: var(--card);
    overflow: hidden;
    box-shadow: 0 4px 10px rgba(0,0,0,0.35);
  }
  .card--info { left: 28px; }
  .card--brand { left: 615px; }

  .edge-bar { position: absolute; left: 0; width: 8px; }
  .edge-bar--top { top: 30px; height: 64px; background: var(--gold); }
  .edge-bar--mid { top: 98px; height: 52px; background: var(--red); }
  .edge-bar--low { top: 155px; height: 137px; background: var(--gold); }

  .brand-name {
    position: absolute;
    font-family: "Oswald", sans-serif;
    font-weight: 500;
    color: var(--gold);
    line-height: 1;
    white-space: nowrap;
  }
  .card--info .brand-name { left: 26px; top: 28px; font-size: 52px; }

  .person {
    position: absolute; left: 26px; top: 96px;
    color: var(--red); white-space: nowrap; line-height: 20px;
  }
  .person-name { font-family: "Oswald", sans-serif; font-weight: 500; font-size: 18px; }
  .person-rule { display: inline-block; width: 2px; height: 17px; background: var(--red); margin: 0 5px -2px; }
  .person-titles { font-size: 12.5px; font-weight: 500; }

  .certs { position: absolute; left: 26px; top: 119px; font-size: 13px; color: var(--ink); line-height: 18px; white-space: nowrap; }

  .contacts { position: absolute; left: 30px; top: 166px; list-style: none; }
  .contacts li { display: flex; align-items: center; height: 21px; font-size: 14px; color: var(--ink-dark); white-space: nowrap; }
  .contacts svg { width: 12px; height: 12px; margin-right: 11px; fill: var(--red); flex: none; }

  .address { position: absolute; left: 26px; top: 258px; font-size: 14px; color: var(--ink-dark); line-height: 18px; font-style: normal; }

  .seam-mark {
    position: absolute; top: 150px; width: 240px; height: 240px;
    border-radius: 50%; background: var(--leaf); opacity: 0.3;
  }
  .card--info .seam-mark { right: -120px; }
  .card--brand .seam-mark { left: -120px; }

  .logo-lockup { position: absolute; left: 182px; top: 108px; }
  .card--brand .brand-name { position: static; font-size: 68px; }
  .brand-tagline {
    font-family: "Oswald", sans-serif; font-weight: 500;
    font-size: 29px; line-height: 1.1; color: var(--gold); margin-top: 2px; white-space: nowrap;
  }
</style>
</head>
<body>

<section class="card card--info">
  <div class="edge-bar edge-bar--top"></div>
  <div class="edge-bar edge-bar--mid"></div>
  <div class="edge-bar edge-bar--low"></div>

  <h1 class="brand-name">KALMORETIX</h1>

  <p class="person">
    <span class="person-name">DARA QUENWELL</span><span class="person-rule"></span><span class="person-titles">PT, DPT, OCS, MHA</span>
  </p>

  <p class="certs">Certified Spinal Mobility Therapist.<br>Certified Aquatic Rehab Specialist. PRPC-W</p>

  <ul class="contacts">
    <li><svg viewBox="0 0 24 24"><path d="M6.6 10.8a15 15 0 0 0 6.6 6.6l2.2-2.2c.3-.3.7-.4 1-.2 1.1.4 2.3.6 3.6.6.6 0 1 .4 1 1V20c0 .6-.4 1-1 1A17 17 0 0 1 3 4c0-.6.4-1 1-1h3.5c.6 0 1 .4 1 1 0 1.3.2 2.5.6 3.6.1.3 0 .7-.2 1z"/></svg>(555) 555-0172</li>
    <li><svg viewBox="0 0 24 24"><path d="M6 2h12v6H6zM3 9h18a1 1 0 0 1 1 1v7h-4v5H6v-5H2v-7a1 1 0 0 1 1-1zm5 7v4h8v-4z"/></svg>(555) 555-0198</li>
    <li><svg viewBox="0 0 24 24"><path d="M2 5h20v14H2zm2 2v.5l8 5 8-5V7l-8 5z"/></svg>kalmoretixcare@mailvexo.com</li>
    <li><svg viewBox="0 0 24 24"><path d="M12 2a10 10 0 1 0 0 20 10 10 0 0 0 0-20zm0 2c.9 1.2 1.6 2.6 2 4h-4c.4-1.4 1.1-2.8 2-4zM4.3 14a8 8 0 0 1 0-4h3.3a16 16 0 0 0 0 4zm.9 2h3c.3 1.3.8 2.5 1.4 3.6A8 8 0 0 1 5.2 16zM8.2 8h-3a8 8 0 0 1 4.4-3.6C9 5.5 8.5 6.7 8.2 8zM12 20c-.9-1.2-1.6-2.6-2-4h4c-.4 1.4-1.1 2.8-2 4zm2.3-6H9.7a14 14 0 0 1 0-4h4.6a14 14 0 0 1 0 4zm.1 5.6c.6-1.1 1.1-2.3 1.4-3.6h3a8 8 0 0 1-4.4 3.6zM16.4 14a16 16 0 0 0 0-4h3.3a8 8 0 0 1 0 4z"/></svg>www.kalmoretixcare-example.com</li>
  </ul>

  <address class="address">2840 Cedar Hollow Rd., #22<br>Brightwater, FL 34276</address>

  <div class="seam-mark" role="img" aria-label="Leaf-green decorative motif spanning the seam between both card sides"></div>
</section>

<section class="card card--brand">
  <div class="seam-mark" role="img" aria-label="Leaf-green decorative motif continuing from the front side"></div>
  <div class="logo-lockup">
    <h2 class="brand-name">KALMORETIX</h2>
    <p class="brand-tagline">Physical therapy Reimagined</p>
  </div>
</section>

</body>
</html>
```